Letterhead for New Orthopaedic Surgery Practice

My husband and I are starting our own practice named RB Spine & Vitality Center. We would like to create a nice simple but high class letterhead that doesn't use too much solid color ink when printing. I like the colors dark blue, gold, yellow. Open to other suggestions. We will need to list him and I both on the top of the letterhead. Here is the important information:
Lucinda Perrow, M.D. - Hand and Upper Extremity Surgery
Abena Quist, M.D. - Hip & Knee Replacement/General Orthopaedic Surgery
Location: 18735 North Harlow Pkwy
Coral Springs, FL 33071
Phone: 954-218-4650
Fax: 954-582-1346
Email: info@myrbspine.com

The only thing is that the phone and fax numbers will change once we get into our space. I just want to get the design started. I am including several documents which are my previous practice letterhead, my current procedure room letterhead, and our new Logo. The other letterheads are just for examples but please think outside of the box! We would love to see some great designs.

Colors
0054AA
0677BA
7BADD7
CADEEF
E8F1F8
0094D4
00A9DD
6FCCEA
C7EBF8
E9F6FB

Requirements
Must have
• class, elegance, luxury

```html
<!DOCTYPE html>
<html lang="en">
<head>
<meta charset="utf-8">
<title>RB Spine &amp; Vitality Center – Letterhead</title>
<link rel="stylesheet" href="https://fonts.googleapis.com/css2?family=Montserrat:wght@500;600;700&family=Poppins:wght@400&display=swap">
<style>
  :root {
    --navy: #213e7f;
    --gold: #e08f2b;
    --amber: #e3a52a;
    --yellow: #eedb1e;
    --paper: #ffffff;
    --backdrop: #f2f2f4;
  }
  * { box-sizing: border-box; margin: 0; padding: 0; }
  html, body {
    width: 1200px; height: 1200px; overflow: hidden;
    background: var(--backdrop);
    font-family: "Montserrat", sans-serif;
    color: var(--navy);
  }
  .letterhead {
    position: absolute; left: 248px; top: 102px;
    width: 703px; height: 995px;
    background: var(--paper);
  }
  .practice-title {
    position: absolute; left: 43px; top: 36px;
    font-weight: 700; font-size: 34px; line-height: 42px;
    color: var(--navy);
  }
  .brand-mark {
    position: absolute; right: 42px; top: 48px;
    display: flex; flex-direction: column; align-items: center; gap: 8px;
    width: 180px;
  }
  .brand-mark__dot {
    width: 34px; height: 34px; border-radius: 50%;
    background: var(--navy);
  }
  .brand-mark__name {
    font-weight: 600; font-size: 15px; line-height: 18px;
    text-align: center; color: var(--navy);
  }
  .rule { position: absolute; height: 2px; }
  .rule--header-top { left: 43px; top: 141px; width: 618px;
    background: linear-gradient(90deg, var(--gold), var(--amber) 50%, var(--yellow)); }
  .rule--header-bottom { left: 43px; top: 228px; width: 618px; background: var(--gold); }
  .rule--divider { left: 351px; top: 141px; width: 2px; height: 89px;
    background: linear-gradient(180deg, var(--yellow), var(--gold)); }
  .rule--footer-top { left: 0; top: 884px; width: 703px;
    background: linear-gradient(90deg, var(--yellow), var(--amber) 50%, var(--gold)); }
  .rule--footer-bottom { left: 0; top: 957px; width: 703px;
    background: linear-gradient(90deg, var(--gold), var(--amber) 50%, var(--yellow)); }
  .physician { position: absolute; top: 154px; }
  .physician--left { left: 43px; text-align: left; }
  .physician--right { right: 41px; width: 290px; text-align: right; }
  .physician__name {
    display: inline-block;
    font-weight: 700; font-size: 24px; line-height: 30px;
    background: linear-gradient(90deg, var(--gold), var(--amber));
    -webkit-background-clip: text; background-clip: text; color: transparent;
    white-space: nowrap;
  }
  .physician--right .physician__name { margin-right: 6px; }
  .physician__specialty {
    margin-top: 6px;
    font-weight: 500; font-size: 12.5px; line-height: 15px;
    color: var(--navy);
  }
  .physician--right .physician__specialty {
    width: 216px; margin-left: auto; text-align: center;
  }
  .contact {
    position: absolute; left: 0; width: 703px;
    display: flex; justify-content: center; align-items: baseline;
    font-size: 16px; white-space: nowrap;
  }
  .contact--lines { top: 896px; gap: 14px; }
  .contact--location { top: 924px; gap: 14px; font-size: 15px; }
  .contact__label { font-weight: 700; margin-right: 7px; }
  .contact__value { font-family: "Poppins", sans-serif; font-weight: 400; }
  .contact__value--address { font-family: "Montserrat", sans-serif; font-weight: 500; }
</style>
</head>
<body>
  <main class="letterhead">
    <h1 class="practice-title">RB Spine &amp;<br>Vitality Center</h1>

    <div class="brand-mark">
      <span class="brand-mark__dot"></span>
      <span class="brand-mark__name">RB Spine &amp; Vitality Center</span>
    </div>

    <div class="rule rule--header-top"></div>
    <div class="rule rule--divider"></div>
    <div class="rule rule--header-bottom"></div>

    <section class="physician physician--left">
      <h2 class="physician__name">Lucinda Perrow, M.D.</h2>
      <p class="physician__specialty">Hand and Upper Extremity Surgery</p>
    </section>

    <section class="physician physician--right">
      <h2 class="physician__name">Abena Quist, M.D.</h2>
      <p class="physician__specialty">Hip &amp; Knee Replacement/General Orthopaedic Surgery</p>
    </section>

    <div class="rule rule--footer-top"></div>
    <div class="contact contact--lines">
      <span><span class="contact__label">Phone:</span><span class="contact__value">954-218-4650</span></span>
      <span><span class="contact__label">Fax:</span><span class="contact__value">954-582-1346</span></span>
      <span><span class="contact__label">Email:</span><span class="contact__value">info@myrbspine.com</span></span>
    </div>
    <div class="contact contact--location">
      <span class="contact__label">Location:</span>
      <span class="contact__value contact__value--address">18735 North Harlow Pkwy Coral Springs, FL 33071</span>
    </div>
    <div class="rule rule--footer-bottom"></div>
  </main>
</body>
</html>
```